Business Card Design Project

We need a business card to reflect the design of our website - just so it all ties in - it has a retro feel and can be found at http://www.velorasoulpair.com
We will need our phone 0437 215 964
Web address, and email velorapair@fernmail.com included
Our catch cry is "Classic Cocktail Music"
Perfect Live Music for Private & Corporate Events, Weddings and Dinner Music
Our names should be included :-
Maribel Thorne / piano & Dennis Holloway / bass
I am now also including our logo so that it can be included (in part or whole) somehow in the design
My partner thinks we should include our logo in some form in the design of the card - i will attach this here for you. I will attach eps but if you prefer another format please let me know
Regards
Mari

```html
<!DOCTYPE html>
<html lang="en">
<head>
<meta charset="utf-8">
<title>Velora Pair – Business Card</title>
<link rel="stylesheet" href="https://fonts.googleapis.com/css2?family=Poiret+One&family=Josefin+Sans:wght@300;400&display=swap">
<style>
  :root {
    --backdrop: #e7e1d8;
    --teal: #6b9f9c;
    --teal-deep: #3e6e6b;
    --mist: #e3e4e7;
    --mist-dark: #cfd1d5;
    --paper: #f7f7f8;
    --ink: #333336;
    --ink-soft: #5a5a5e;
    --seal: #3b3b3d;
    --cream: #eee1bf;
  }
  * { box-sizing: border-box; margin: 0; padding: 0; }
  html, body { width: 1200px; height: 417px; overflow: hidden; }
  body { background: var(--backdrop); position: relative; font-family: "Josefin Sans", sans-serif; }

  .card {
    position: absolute; top: 54px; width: 540px; height: 309px;
    overflow: hidden; box-shadow: 0 3px 10px rgba(0,0,0,.18);
  }
  .card--front { left: 40px; background: var(--mist); }
  .card--back { left: 620px; background: var(--paper); }

  .band { position: absolute; left: 0; width: 100%; background: var(--teal); }
  .band::before, .band::after {
    content: ""; position: absolute; left: 0; right: 0;
    border-top: 1.5px dashed var(--cream); opacity: .85;
  }
  .card--front .band { top: 0; height: 126px; }
  .card--front .band::before { top: 8px; }
  .card--front .band::after { bottom: 8px; }
  .card--back .band { top: 178px; height: 131px; }
  .card--back .band::before { top: 8px; }
  .card--back .band::after { bottom: 12px; }

  .pattern-field {
    position: absolute; top: 126px; left: 0; width: 100%; height: 183px;
    background: linear-gradient(180deg, var(--mist) 0%, var(--mist-dark) 100%);
  }

  .seal { position: absolute; }
  .card--front .seal { left: 38px; top: 64px; width: 120px; height: 120px; }
  .card--back .seal { left: 376px; top: 118px; width: 130px; height: 130px; }

  .catchcry {
    position: absolute; left: 14px; right: 14px; bottom: 16px;
    font-family: "Poiret One", sans-serif; font-size: 37px; font-weight: 400;
    color: var(--ink); text-transform: uppercase; letter-spacing: 0;
    white-space: nowrap; line-height: 1;
  }

  .names {
    position: absolute; left: 14px; top: 20px;
    font-weight: 300; font-size: 23.5px; color: var(--ink); white-space: nowrap;
  }
  .address, .contact {
    position: absolute; left: 16px; font-weight: 300; font-size: 9.5px;
    line-height: 13px; color: var(--ink-soft); list-style: none;
  }
  .address { top: 60px; }
  .contact { top: 118px; }
  .tagline {
    position: absolute; left: 14px; bottom: 17px;
    font-size: 10.6px; text-transform: uppercase; color: var(--teal-deep);
    white-space: nowrap; letter-spacing: .2px;
  }
</style>
</head>
<body>

<section class="card card--front" aria-label="Card front">
  <div class="band"></div>
  <div class="pattern-field" role="img" aria-label="Repeating pattern of faint circular monogram medallions"></div>
  <svg class="seal" viewBox="0 0 120 120" aria-label="Velora Pair">
    <circle cx="60" cy="60" r="58" fill="var(--teal)"/>
    <circle cx="60" cy="60" r="46" fill="var(--seal)"/>
    <text x="60" y="56" text-anchor="middle" font-family="Josefin Sans, sans-serif" font-size="17" fill="var(--cream)">Velora</text>
    <text x="60" y="76" text-anchor="middle" font-family="Josefin Sans, sans-serif" font-size="17" fill="var(--cream)">Pair</text>
  </svg>
  <h1 class="catchcry">Classic Cocktail Music</h1>
</section>

<section class="card card--back" aria-label="Card back">
  <h2 class="names">Maribel Thorne/Piano &amp; Dennis Holloway/Bass</h2>
  <ul class="address">
    <li>12/48 Kestrel Lane</li>
    <li>Paddington QLD</li>
    <li>4064 Australia</li>
  </ul>
  <ul class="contact">
    <li>P: 0437 215 964</li>
    <li>E: velorapair@fernmail.com</li>
    <li>W: http://www.velorasoulpair.com</li>
  </ul>
  <div class="band"></div>
  <svg class="seal" viewBox="0 0 120 120" aria-label="Velora Pair">
    <circle cx="60" cy="60" r="58" fill="var(--teal)"/>
    <circle cx="60" cy="60" r="46" fill="var(--seal)"/>
    <text x="60" y="56" text-anchor="middle" font-family="Josefin Sans, sans-serif" font-size="17" fill="var(--cream)">Velora</text>
    <text x="60" y="76" text-anchor="middle" font-family="Josefin Sans, sans-serif" font-size="17" fill="var(--cream)">Pair</text>
  </svg>
  <p class="tagline">Perfect live music for private &amp; corporate events, weddings and dinner music</p>
</section>

</body>
</html>
```